Business Card

We need some ideas for corporate business cards. I'm interested in a double sided card, with one side featuring our corporate logo, the other side with employee information.

Corporate colors, logo etc. available at www.brivalo.com

Industry/Entity Type

Business

Requirements
Must have
• The "Brivalo" logo with stylized "O"

Nice to have
• Preferred font is calibri

```html
<!DOCTYPE html>
<html lang="en">
<head>
<meta charset="utf-8">
<title>Brivalo – Business Card</title>
<link rel="stylesheet" href="https://fonts.googleapis.com/css2?family=Carlito:wght@400;700&display=swap">
<style>
  :root {
    --brand-blue: #4a6796;
    --brand-blue-dark: #3f5b8a;
    --brand-blue-light: #8fb1de;
    --ink: #4b679a;
    --paper: #ffffff;
  }
  html, body {
    margin: 0;
    padding: 0;
    width: 1200px;
    height: 701px;
    overflow: hidden;
    background: var(--paper);
  }
  .card {
    position: relative;
    width: 1200px;
    height: 701px;
    background: var(--paper);
    font-family: "Carlito", "Calibri", sans-serif;
    color: var(--ink);
    overflow: hidden;
  }
  .card__art {
    position: absolute;
    inset: 0;
    width: 1200px;
    height: 701px;
  }
  .identity {
    position: absolute;
    left: 43px;
    top: 100px;
  }
  .identity__name {
    margin: 0;
    font-size: 51px;
    font-weight: 400;
    line-height: 1;
    letter-spacing: 0.2px;
  }
  .identity__role {
    margin: 10px 0 0 1px;
    font-size: 25px;
    line-height: 1;
  }
  .contact {
    position: absolute;
    left: 44px;
    top: 268px;
    margin: 0;
    padding: 0;
    list-style: none;
    font-size: 25px;
    line-height: 29px;
  }
  .contact__item {
    display: flex;
    align-items: flex-start;
    margin-bottom: 21px;
  }
  .contact__icon {
    width: 30px;
    height: 29px;
    margin-right: 29px;
    flex: none;
    fill: var(--brand-blue);
  }
  .contact__address {
    font-style: normal;
  }
</style>
</head>
<body>
<main class="card">
  <svg class="card__art" viewBox="0 0 1051 614" preserveAspectRatio="none" aria-hidden="false">
    <defs>
      <radialGradient id="brandGlow" cx="760" cy="300" r="330" gradientUnits="userSpaceOnUse">
        <stop offset="0" stop-color="var(--brand-blue-light)" style="stop-color:#8fb1de"/>
        <stop offset="0.55" stop-color="#5f7fb0"/>
        <stop offset="1" stop-color="#4a6796"/>
      </radialGradient>
    </defs>
    <line class="divider" x1="27" y1="198" x2="478" y2="198" stroke="#4a6796" stroke-width="1.6"/>
    <ellipse class="brand-panel__ring" cx="872" cy="307" rx="414" ry="366" fill="none" stroke="#4a6796" stroke-width="3"/>
    <ellipse class="brand-panel" cx="872" cy="307" rx="400" ry="354" fill="url(#brandGlow)"/>
    <text class="brand-panel__name" x="768" y="334" text-anchor="middle"
          font-family="Carlito, Calibri, sans-serif" font-size="90" font-weight="400"
          letter-spacing="20" fill="#ffffff">BRIVALO</text>
  </svg>

  <header class="identity">
    <h1 class="identity__name">Daniel Hart</h1>
    <p class="identity__role">Managing Director</p>
  </header>

  <ul class="contact">
    <li class="contact__item">
      <svg class="contact__icon" viewBox="0 0 24 24" aria-label="Phone" role="img">
        <path d="M6.6 2.2c.5-.3 1.1-.2 1.5.3l2.2 3c.3.5.3 1.1-.1 1.5L8.8 8.4c.9 2.6 3 4.9 5.4 6.2l1.4-1.4c.4-.4 1-.5 1.5-.2l3.1 2c.5.3.7 1 .4 1.5l-1.3 2.6c-.4.8-1.3 1.2-2.2 1C10.7 18.8 5.4 13.3 3.9 6.8c-.2-.9.2-1.8 1-2.3z"/>
      </svg>
      <span>001 002 4815962</span>
    </li>
    <li class="contact__item">
      <svg class="contact__icon" viewBox="0 0 24 24" aria-label="Email" role="img">
        <path d="M2 6.5h20v11H2z M3.5 8v.3l8.5 5.4 8.5-5.4V8l-8.5 5.2z" fill-rule="evenodd"/>
      </svg>
      <span>d.hart@brivalo.com</span>
    </li>
    <li class="contact__item">
      <svg class="contact__icon" viewBox="0 0 24 24" aria-label="Address" role="img">
        <path d="M12 2.5 1.5 11.5l1.3 1.4L12 5.1l9.2 7.8 1.3-1.4L18.5 8V3.5h-2.5v2.4z M4.5 13.5 12 7.2l7.5 6.3V21h-5.3v-5h-4.4v5H4.5z"/>
      </svg>
      <address class="contact__address">Brivalo<br>14 Harlow Lane,<br>Westgate Business Park,<br>Dublin</address>
    </li>
  </ul>
</main>
</body>
</html>
```